Finance web application design

We need a design for a new responsive finance web application. It should look uber professional and modern.

Inspiration and design we like:

website:
http://www.brennickhale.com/

The application presented here:
http://markets.pelvantgrid.com/en/products/tools-applications/trading-investment-tools/zarvo-trading-software.html

https://apps.quillstore.example/us/app/ferncastle-for-tablet/id582917463?mt=8

The application presented here (Slatepad version):
https://apps.quillstore.example/en/app/trevik-forex-trading/id649205318?mt=8&utm_source=trevikButton

Target Market(s)

Private Investors

Industry/Entity Type

Finance

Number of Pages Required

5+ page

Font styles to use
Other font styles liked:
• Nobile

Requirements
Must have
• Colors for "up" changes: green
• Colors for "down" changes: red
• Fonts in tables must be very easy to read -
• Deliver design for all pages attached.
Nice to have
• A dark (gray) background
• Graphs should be shaded and partly transparent - orange or blue
• White text as "normal" - orange text / blue text for headers
Should not have
• White background

```html
<!DOCTYPE html>
<html lang="en">
<head>
<meta charset="utf-8">
<title>Ledgerwick.io – NRX Index</title>
<link href="https://fonts.googleapis.com/css2?family=Open+Sans:wght@400;600;700&display=swap" rel="stylesheet">
<style>
:root{
  --page:#1f282e;
  --topbar:#29343b;
  --titlebar:#2b3a42;
  --body:#0e1215;
  --panel:#0b0e11;
  --line:#2a343c;
  --blue:#0077ad;
  --blue-text:#1583bd;
  --orange:#f19a37;
  --white:#ffffff;
  --muted:#c9d1d6;
  --thead:#1a1f2b;
}
*{box-sizing:border-box;margin:0;padding:0}
html,body{width:1200px;height:1108px;overflow:hidden}
body{background:var(--page);font-family:"Open Sans",Arial,sans-serif;color:var(--white);position:relative}
.abs{position:absolute}
.topbar{left:0;top:0;width:1200px;height:80px;background:var(--topbar)}
.brand{left:24px;top:22px;display:flex;align-items:center;gap:6px;font-size:27px;font-weight:700;color:var(--orange);letter-spacing:-.3px}
.brand-mark{width:12px;height:12px;background:var(--orange)}
.nav{left:257px;top:30px;display:flex;gap:18px;font-size:14.5px;font-weight:600}
.search{left:796px;top:21px;width:226px;height:37px;border:1px solid #47535b;border-radius:19px;font-size:14px;color:#7d8890;padding:9px 0 0 22px}
.search svg{position:absolute;right:14px;top:9px}
.user{left:1043px;top:27px;display:flex;align-items:center;gap:9px;font-size:14.5px;font-weight:600}
.avatar{width:25px;height:25px;border-radius:50%;background:radial-gradient(circle at 50% 40%,#b99a86,#5b4d46)}
.power{left:1157px;top:30px}
.card{left:25px;top:98px;width:1150px;height:945px;background:var(--body)}
.titlebar{left:25px;top:98px;width:1150px;height:78px;background:var(--titlebar);border-bottom:1px solid #3b4a53}
.title{left:53px;top:121px;font-size:24px;font-weight:600}
.change{left:281px;top:126px;font-size:17px;font-weight:600;color:var(--orange)}
.panel{background:var(--panel);border:1px solid var(--line)}
.panel-head{height:46px;background:var(--blue);font-size:20px;font-weight:600;padding:8px 22px}
.tabs{left:50px;top:204px;width:580px;height:49px;background:var(--blue);display:flex;justify-content:flex-end}
.tabs span{padding:15px 8px 0;font-size:16px;font-weight:600;border-left:1px solid #0a6a98}
.tabs .on{background:var(--body);color:var(--blue-text)}
.field{border:1px solid #3a444b;border-radius:2px;background:var(--panel);font-size:16px;padding:17px 18px;height:57px}
.dd{position:absolute;right:-1px;top:-1px;width:53px;height:57px;background:var(--blue);display:flex;align-items:center;justify-content:center}
.h-blue{color:var(--blue-text);font-size:20px;font-weight:600}
.copy{font-size:14px;line-height:25px}
.cost-table{left:76px;top:831px;width:273px;border:1px solid #3a444b;font-size:14px}
.cost-row{display:flex;justify-content:space-between;align-items:center;padding:0 12px 0 10px;border-bottom:1px solid #3a444b}
.cost-row:last-child{border-bottom:0}
.cost-row .v{color:var(--orange);font-size:13.5px}
.date{color:var(--blue-text);font-size:12px}
.risk{left:404px;top:837px;font-size:14px;line-height:30px}
.perf{left:662px;top:693px;width:489px;border-collapse:collapse;font-size:13px}
.perf td{border:1px solid var(--line);text-align:center;width:50%;height:41.7px}
.perf tr.thead td{background:var(--thead);height:40px}
.perf td.v{color:var(--orange)}
.footer{left:0;top:1067px;width:1200px;text-align:center;font-size:14px}
</style>
</head>
<body>
<header class="abs topbar"></header>
<div class="abs brand"><span class="brand-mark"></span>Ledgerwick.io</div>
<nav class="abs nav"><span>Dashboard</span><span>Strategies</span><span>Portfolios</span><span>Market Data</span><span>Cust Inst.</span><span>User</span></nav>
<div class="abs search">Search for fund...
<svg width="18" height="18" viewBox="0 0 18 18"><circle cx="7" cy="7" r="5.5" fill="none" stroke="#1583bd" stroke-width="2"/><path d="M11 11l5 5" stroke="#1583bd" stroke-width="2.5" stroke-linecap="round"/></svg></div>
<div class="abs user"><span class="avatar" role="img" aria-label="User avatar"></span>John Doe</div>
<svg class="abs power" width="18" height="19" viewBox="0 0 18 19"><path d="M5 4.5a7 7 0 1 0 8 0" fill="none" stroke="#1583bd" stroke-width="2" stroke-linecap="round"/><path d="M9 1.5v7" stroke="#1583bd" stroke-width="2" stroke-linecap="round"/></svg>

<main class="abs card"></main>
<div class="abs titlebar"></div>
<h1 class="abs title">NRX Index - 601,45</h1>
<div class="abs change">0,42 (+1,29%)</div>

<!-- chart -->
<div class="abs panel" style="left:50px;top:204px;width:581px;height:310px"></div>
<div class="abs tabs"><span>1M</span><span>6M</span><span>YTD</span><span class="on">1Y</span><span>3Y</span><span>5Y</span><span>Max</span></div>
<svg class="abs" style="left:50px;top:254px" width="580" height="259" viewBox="0 0 580 259">
  <g stroke="#1c242a" stroke-width="1">
    <path d="M28 24V226M68 24V226M108 24V226M148 24V226M188 24V226M228 24V226M268 24V226M308 24V226M348 24V226M388 24V226M428 24V226M468 24V226M508 24V226M548 24V226"/>
    <path d="M28 24H555M28 64H555M28 104H555M28 144H555M28 184H555" stroke-dasharray="3 3"/>
  </g>
  <path d="M28 226 108 104 188 127 308 104 388 66 428 103 508 24 508 226Z" fill="#0e5a82" fill-opacity=".45"/>
  <path d="M28 226 108 145 188 104 268 144 388 104 428 66 468 103 508 66 508 226Z" fill="#8a4f1c" fill-opacity=".55"/>
  <path d="M28 226H555" stroke="#3a444b"/>
  <path d="M28 226 108 104 188 127 308 104 388 66 428 103 508 24" fill="none" stroke="#1583bd" stroke-width="1.5"/>
  <path d="M28 226 108 145 188 104 268 144 388 104 428 66 468 103 508 66" fill="none" stroke="#f19a37" stroke-width="1.5"/>
  <g fill="#0e1215" stroke="#0f6a99" stroke-width="3">
    <circle cx="108" cy="104" r="4.5"/><circle cx="188" cy="127" r="4.5"/><circle cx="308" cy="104" r="4.5"/><circle cx="388" cy="66" r="4.5"/><circle cx="428" cy="103" r="4.5"/><circle cx="508" cy="24" r="4.5"/>
  </g>
  <g fill="#0e1215" stroke="#f19a37" stroke-width="2.5">
    <circle cx="108" cy="145" r="4"/><circle cx="188" cy="104" r="4"/><circle cx="268" cy="144" r="4"/><circle cx="388" cy="104" r="4"/><circle cx="428" cy="66" r="4"/><circle cx="468" cy="103" r="4"/><circle cx="508" cy="66" r="4"/>
  </g>
</svg>

<!-- fund details -->
<section class="abs panel" style="left:50px;top:545px;width:581px;height:475px"></section>
<h2 class="abs h-blue" style="left:76px;top:570px">Fund Details</h2>
<p class="abs copy" style="left:76px;top:615px;width:525px">Lorem ipsum dolor sit amet, consectetur adipiscing elit. Sed pretium, massa ut elementum viverra, arcu dui aliquet sapien, sed mollis nunc diam eget sapien. Vivamus sed luctus dolor. Ut quis diam bibendum, pretium tellus a, elementum magna.</p>
<div class="abs" style="left:76px;top:730px;width:527px;height:1px;background:#3a444b"></div>
<div class="abs" style="left:76px;top:785px;width:527px;height:1px;background:#3a444b"></div>
<div class="abs" style="left:377px;top:731px;width:1px;height:264px;background:#3a444b"></div>
<div class="abs h-blue" style="left:76px;top:745px">ISIN</div>
<div class="abs" style="left:150px;top:746px;font-size:17px;font-weight:600">NO0010073216</div>
<div class="abs h-blue" style="left:405px;top:745px">Rating</div>
<svg class="abs" style="left:507px;top:749px" width="96" height="18" viewBox="0 0 96 18">
  <defs><path id="star" d="M9 0l2.6 5.8 6.4.6-4.8 4.3 1.4 6.3L9 13.8 3.4 17l1.4-6.3L0 6.4l6.4-.6z"/></defs>
  <use href="#star" fill="#f19a37"/><use href="#star" x="19.5" fill="#f19a37"/><use href="#star" x="39" fill="#f19a37"/><use href="#star" x="58.5" fill="#f19a37"/><use href="#star" x="78" fill="#2c3640"/>
</svg>
<div class="abs h-blue" style="left:76px;top:800px">Cost</div>
<div class="abs h-blue" style="left:404px;top:800px">Risk</div>
<div class="abs cost-table">
  <div class="cost-row" style="height:46px"><span>Marks Kjopsavg</span><span class="v" style="margin-right:32px">---</span></div>
  <div class="cost-row" style="height:68px"><span>Lopende Kostnader<br><span class="date">21.01.2014</span></span><span class="v" style="margin-right:6px">1,00%</span></div>
  <div class="cost-row" style="height:47px"><span>Resultatbasert Avg.</span><span class="v">10,00%</span></div>
</div>
<div class="abs risk">Sharp<br>Avr Return<br>Std Dev</div>

<!-- indicators -->
<section class="abs panel" style="left:662px;top:204px;width:490px;height:230px"><div class="panel-head">Indicators</div></section>
<div class="abs field" style="left:686px;top:273px;width:328px">Moving Average<span class="dd"><svg width="22" height="14" viewBox="0 0 22 14"><path d="M2 2l9 9 9-9" fill="none" stroke="#fff" stroke-width="2.5"/></svg></span></div>
<div class="abs field" style="left:1035px;top:273px;width:94px">50</div>
<div class="abs field" style="left:686px;top:351px;width:328px">Moving Average<span class="dd"><svg width="22" height="14" viewBox="0 0 22 14"><path d="M2 2l9 9 9-9" fill="none" stroke="#fff" stroke-width="2.5"/></svg></span></div>
<div class="abs field" style="left:1035px;top:351px;width:94px">50</div>

<!-- compare -->
<section class="abs panel" style="left:662px;top:464px;width:490px;height:150px"><div class="panel-head">Compare</div></section>
<div class="abs field" style="left:686px;top:533px;width:443px">Search for instruments by name....
<svg style="position:absolute;right:14px;top:17px" width="26" height="26" viewBox="0 0 26 26"><circle cx="10" cy="10" r="7.5" fill="none" stroke="#1583bd" stroke-width="2.5"/><path d="M15.5 15.5l8 8" stroke="#1583bd" stroke-width="3.5" stroke-linecap="round"/></svg></div>

<!-- performance -->
<section class="abs panel" style="left:662px;top:648px;width:490px;height:372px"><div class="panel-head">Performance</div></section>
<table class="abs perf">
  <tr class="thead"><td></td><td></td></tr>
  <tr><td>1W</td><td class="v">+2,04%</td></tr>
  <tr><td>1M</td><td class="v">+1,04%</td></tr>
  <tr><td>3M</td><td class="v">+3,04%</td></tr>
  <tr><td>6M</td><td class="v">+6,04%</td></tr>
  <tr><td>YTD</td><td class="v">+10,04%</td></tr>
  <tr><td>1Y</td><td class="v">+23,04%</td></tr>
  <tr><td>3Y Ann</td><td class="v">+14,04%</td></tr>
</table>

<footer class="abs footer">Copyright © 2014 Ledgerwick.io. All Rights Reserved</footer>
</body>
</html>
```